Business Card Design

We are an IT staffing and consulting company providing IT solutions and resources to our clients.

Industry/Entity Type

Business

Contact Information for Business Card

Ramesh Tulavarthi
Vice President

BrightNode Inc
48215 Harrowmere Court Square, suite 700
Hollin Ridge, VA 20199
Direct: 571-555-0193
Mobile: 571-555-0147
Email: Ramesh@brightnodeinc.com
Fax: 703-555-0162
www.brightnodeinc.com

```html
<!DOCTYPE html>
<html lang="en">
<head>
<meta charset="utf-8">
<title>BrightNode Inc — Business Card</title>
<link href="https://fonts.googleapis.com/css2?family=Open+Sans:wght@400;600&family=Oswald:wght@500&display=swap" rel="stylesheet">
<style>
  :root {
    --backdrop: #e9e6e2;
    --charcoal: #2f2f31;
    --paper: #ffffff;
    --brand-red: #b5121b;
    --text-light: #f2f2f2;
    --text-muted: #9a9a9c;
  }
  * { box-sizing: border-box; margin: 0; padding: 0; }
  html, body { width: 1200px; height: 915px; overflow: hidden; }
  body {
    background: var(--backdrop);
    font-family: "Open Sans", Arial, sans-serif;
    position: relative;
  }
  .card {
    position: absolute;
    top: 128px;
    width: 420px;
    height: 660px;
    border-radius: 34px;
    overflow: hidden;
    background: var(--charcoal);
    box-shadow: 0 10px 30px rgba(0,0,0,0.25);
  }
  .card--back { left: 140px; }
  .card--front { left: 640px; }

  /* Back */
  .back-brand {
    position: absolute;
    top: 300px; left: 0; right: 0;
    display: flex; align-items: center; justify-content: center; gap: 12px;
  }
  .brand-dot {
    width: 16px; height: 16px; border-radius: 50%;
    background: var(--brand-red);
    flex: none;
  }
  .back-brand .brand-name {
    font-size: 40px; font-weight: 400; color: var(--text-muted);
    letter-spacing: 1px;
  }
  .footer-band {
    position: absolute; left: 0; right: 0; bottom: 0;
    height: 52px; background: var(--brand-red);
    display: flex; align-items: center; justify-content: center;
    color: var(--text-light); font-size: 18px; font-weight: 600;
  }

  /* Front */
  .front-top {
    position: absolute; top: 0; left: 0; right: 0; height: 215px;
    background: var(--paper);
  }
  .front-brand {
    position: absolute; top: 88px; left: 60px;
    display: flex; align-items: center; gap: 12px;
  }
  .front-brand .brand-name {
    font-size: 40px; font-weight: 400; color: var(--brand-red);
    letter-spacing: 1px;
  }
  .divider { position: absolute; top: 195px; left: 0; width: 420px; height: 40px; }
  .contact-name {
    position: absolute; top: 255px; left: 40px;
    font-family: "Oswald", "Arial Narrow", sans-serif; font-weight: 500;
    font-size: 26px; line-height: 36px; text-transform: uppercase; color: var(--text-light);
    letter-spacing: 0.5px;
  }
  .contact-name .first { color: var(--brand-red); }
  .contact-title {
    position: absolute; top: 296px; left: 42px;
    font-size: 18px; line-height: 24px; color: var(--text-light);
  }
  .contact-address {
    position: absolute; top: 336px; left: 42px; width: 360px;
    font-size: 16px; line-height: 24px; color: var(--text-light);
  }
  .contact-list {
    position: absolute; left: 42px; list-style: none;
    font-size: 17px; color: var(--text-light);
  }
  .contact-list--phones { top: 428px; }
  .contact-list--web { top: 538px; }
  .contact-list li { display: flex; align-items: center; gap: 16px; height: 30px; }
  .contact-list svg { width: 16px; height: 16px; fill: var(--text-light); flex: none; }
  .front-band { height: 40px; }
</style>
</head>
<body>

<section class="card card--back" aria-label="Card back">
  <div class="back-brand">
    <span class="brand-dot"></span>
    <span class="brand-name">BrightNode</span>
  </div>
  <div class="footer-band">www.brightnodeinc.com</div>
</section>

<section class="card card--front" aria-label="Card front">
  <div class="front-top">
    <div class="front-brand">
      <span class="brand-dot"></span>
      <span class="brand-name">BrightNode</span>
    </div>
  </div>
  <svg class="divider" viewBox="0 0 420 40" aria-hidden="true">
    <polygon points="0,20 420,20 420,0 0,0" fill="#ffffff"/>
    <path d="M30 18 Q210 8 400 0 L400 3 Q210 14 30 20 Z" fill="#b5121b"/>
    <polygon points="198,20 222,20 210,30" fill="#ffffff"/>
  </svg>

  <h1 class="contact-name"><span class="first">Ramesh</span> Tulavarthi</h1>
  <p class="contact-title">Vice President</p>
  <p class="contact-address">48215 Harrowmere Court Square,<br>suite 700 Hollin Ridge, VA 20199</p>

  <ul class="contact-list contact-list--phones">
    <li>
      <svg viewBox="0 0 16 16" aria-label="Direct"><path d="M3 1l3 3-2 2c1 2 3 4 5 5l2-2 3 3-2 3C7 15 1 9 1 3z"/></svg>
      571-555-0193
    </li>
    <li>
      <svg viewBox="0 0 16 16" aria-label="Mobile"><path d="M4 0h8v16H4zM5 2v9h6V2zM7 13h2v1H7z" fill-rule="evenodd"/></svg>
      571-555-0147
    </li>
    <li>
      <svg viewBox="0 0 16 16" aria-label="Fax"><path d="M4 1h8v4H4zM1 6h14v6h-3v3H4v-3H1zM5 10v4h6v-4z" fill-rule="evenodd"/></svg>
      703-555-0162
    </li>
  </ul>

  <ul class="contact-list contact-list--web">
    <li>
      <svg viewBox="0 0 16 16" aria-label="Email"><path d="M1 3h14v10H1zM2 4l6 5 6-5z" fill-rule="evenodd"/></svg>
      Ramesh@brightnodeinc.com
    </li>
    <li>
      <svg viewBox="0 0 16 16" aria-label="Website"><circle cx="8" cy="8" r="7"/><path d="M1 8h14M8 1c-3 3-3 11 0 14M8 1c3 3 3 11 0 14" stroke="#2f2f31" stroke-width="1" fill="none"/></svg>
      www.brightnodeinc.com
    </li>
  </ul>

  <div class="footer-band front-band"></div>
</section>

</body>
</html>
```